Personal contact Business card design needed

I work in the Property Industry - specifically Property Management.

I need a card I can hand out to colleagues at networking events, meetings, training courses etc. that will provide my contact details.

Target Market(s)

Professional colleagues / potential clients / employers

Industry/Entity Type

Training

Contact Information for Business Card

I need a simple and professional card to give to professional network contacts at meetings, interviews etc.

The card should include my photograph, name, mobile number, email address and Careerloom address.

I would like appropriate professional colours. Something feminine but not too 'frilly' or 'girly'

Requirements
Must have
• Photograph of myself.
I want it to be simple,perhaps a small icon for each contact detail such as
Email icon
Careerloom icon
Mobile number

```html
<!DOCTYPE html>
<html lang="en">
<head>
<meta charset="utf-8">
<title>Nadia Vale – Business Card</title>
<link href="https://fonts.googleapis.com/css2?family=Comfortaa:wght@300;400;700&family=Raleway:wght@700&family=Nothing+You+Could+Do&display=swap" rel="stylesheet">
<style>
  :root {
    --plum: #93286f;
    --plum-dark: #7a1f5c;
    --paper: #f1f0ee;
    --ink: #2a2a2a;
    --grey: #6b6b6b;
    --charcoal: #3a3a3a;
    --stage: #e4e2df;
    --hand: "Nothing You Could Do", cursive;
    --sans: "Comfortaa", sans-serif;
  }
  * { box-sizing: border-box; margin: 0; padding: 0; }
  html, body { width: 1200px; height: 873px; overflow: hidden; }
  body {
    background: var(--stage);
    display: flex; align-items: center; justify-content: center; gap: 60px;
    font-family: var(--sans);
  }
  .card {
    position: relative; width: 520px; height: 300px; overflow: hidden;
    box-shadow: 0 6px 18px rgba(0,0,0,.15);
  }
  .card--front { background: var(--paper); color: var(--ink); }
  .card--back { background: var(--plum); }

  .front-band { position: absolute; left: 0; bottom: 0; width: 520px; height: 300px; }

  .name-label { position: absolute; left: 26px; top: 20px; font: 700 16px "Raleway", sans-serif; }
  .name { position: absolute; left: 26px; top: 40px; font: 26px var(--hand); color: var(--plum); white-space: nowrap; }
  .this-is-me { position: absolute; left: 26px; top: 82px; font: 17px var(--hand); }
  .photo {
    position: absolute; left: 150px; top: 76px; width: 112px; height: 84px;
    background: linear-gradient(160deg, #cfcac6, #4a3a38 60%, #2a1f1f);
  }
  .doodle { position: absolute; fill: none; stroke: var(--ink); stroke-width: 2; stroke-linecap: round; }

  .profile-note { position: absolute; left: 26px; top: 176px; font: 17px var(--hand); white-space: nowrap; }
  .profile-link { position: absolute; left: 26px; top: 214px; display: flex; align-items: center; gap: 6px; font-size: 11px; color: var(--grey); white-space: nowrap; }
  .profile-link .square { width: 9px; height: 9px; background: var(--ink); }
  .profile-link .brand { font-weight: 700; color: var(--ink); }
  .profile-link .url b { color: var(--ink); }

  .contact-title { position: absolute; left: 330px; top: 48px; font: 18px var(--hand); }
  .contact-panel {
    position: absolute; left: 322px; top: 84px; width: 198px; height: 62px;
    background: var(--plum); border-left: 10px solid var(--charcoal);
    color: #fff; font-size: 11.5px; padding: 10px 0 0 10px;
    display: flex; flex-direction: column; gap: 8px;
  }
  .contact-row { display: flex; align-items: center; gap: 8px; white-space: nowrap; }
  .contact-row svg { width: 13px; height: 13px; fill: none; stroke: #fff; stroke-width: 1.6; }

  .back-name { position: absolute; right: 46px; bottom: 34px; font: 58px var(--hand); color: #fff; }
</style>
</head>
<body>
  <section class="card card--front">
    <svg class="front-band" viewBox="0 0 520 300" aria-hidden="true">
      <polygon points="0,262 300,262 340,282 520,282 520,300 0,300" fill="var(--plum)"/>
    </svg>

    <p class="name-label">Name:</p>
    <p class="name">Nadia Vale</p>
    <svg class="doodle" style="left:180px;top:40px" width="40" height="30" viewBox="0 0 40 30"><path d="M4 8 C20 0 32 8 26 20 M20 16 l6 5 l4 -7"/></svg>
    <p class="this-is-me">This is me:</p>
    <svg class="doodle" style="left:272px;top:104px" width="40" height="34" viewBox="0 0 40 34"><path d="M30 4 C40 18 28 30 8 24 M14 18 l-6 6 l8 4"/></svg>
    <div class="photo" role="img" aria-label="Portrait photograph of Nadia Vale"></div>

    <p class="profile-note">And this is my Careerloom profile</p>
    <div class="profile-link">
      <span class="square"></span><span class="brand">Careerloom</span>
      <span class="url">au.careerloom.com/in/<b>nadiavale/</b></span>
    </div>
    <svg class="doodle" style="left:318px;top:184px" width="44" height="40" viewBox="0 0 44 40"><path d="M20 4 C42 8 40 34 14 30 M20 24 l-7 6 l8 5"/></svg>

    <p class="contact-title">contact me</p>
    <div class="contact-panel">
      <div class="contact-row">
        <svg viewBox="0 0 14 14"><path d="M3 1 h3 l1 3 l-2 1 a7 7 0 0 0 4 4 l1 -2 l3 1 v3 a1 1 0 0 1 -1 1 A11 11 0 0 1 2 2 a1 1 0 0 1 1 -1z"/></svg>
        <span>0400 555 123</span>
      </div>
      <div class="contact-row">
        <svg viewBox="0 0 14 14"><rect x="1" y="3" width="12" height="8"/><path d="M1 3 l6 5 l6 -5"/></svg>
        <span>nadia@mailbox.com.au</span>
      </div>
    </div>
  </section>

  <section class="card card--back">
    <p class="back-name">Nadia</p>
  </section>
</body>
</html>
```